Wordpress Design Project (Darvy)

We need a wordpress design for an established auction and real estate company based in Pennsylvania. The winning design will incorporate a professional layout with and company logo in a very simple and clean layout.

Industry/Entity Type

Real Estate

Requirements
Must have
• Navigation:
1) Home; 2) Auctions; 3) Appraisals; 4) Real Estate; 5) FAQ; 6) About Us; 7) Contact Us.

Site will have overall layout of https://www.plumvesta.com/featured/regions/the-northeast. Home page will have logo and navigation at top. The navigation bar will also have social media icons (facebook, Google+, RSS, twitter) inside it. There will be text in the content area - use lorem ipsum. The image attached will be used below text (auctions.jpg) . Footer will have smaller company loogo, the attached affiliation logos and social media icons.

Logo attached. Color scheme will be black, gray, and red as accent color.
Nice to have
• navigation will have dropdowns, nice to have one represented - under auctions 'All Auctions' will be dropdown.

```html
<!DOCTYPE html>
<html lang="en">
<head>
<meta charset="utf-8">
<title>Darvy – Real Estate Services</title>
<link rel="stylesheet" href="https://fonts.googleapis.com/css2?family=Open+Sans:wght@300;400;600;700&family=Roboto:wght@400;500;700&display=swap">
<style>
:root{
  --tan:#d5ad82;
  --cream:#fdf5e2;
  --ribbon:#efe4c6;
  --ribbon-edge:#dccfa8;
  --red:#d63322;
  --brand-red:#e0281e;
  --maroon:#4a0d08;
  --ink:#3a3a3a;
  --muted:#666;
  --frame:#ece2cb;
  --footer:#4b4443;
  --photo:#b7b29c;
  --photo-alt:#a9ad93;
  --fb:#3b5a9a;
  --gp:#d53f2f;
  --tw:#3ea6dc;
  --rss:#ee9a2b;
}
*{box-sizing:border-box;margin:0;padding:0}
html,body{width:1200px;height:949px;overflow:hidden}
body{background:var(--tan);font-family:"Open Sans",sans-serif;color:var(--ink);position:relative}
.top-band{position:absolute;left:0;top:0;width:1200px;height:20px;background:linear-gradient(#a8150c,#7d0e07);border-bottom:2px solid #c9998a}
.page{position:absolute;left:161px;top:20px;width:892px;height:929px;background:var(--cream)}
.abs{position:absolute}

.brand{left:20px;top:16px;display:flex;align-items:center;gap:12px}
.brand-mark{width:74px;height:74px;background:var(--brand-red);border-radius:6px}
.brand-name{font-weight:700;font-size:44px;color:#1c1c1c;letter-spacing:1px}

.social{left:731px;top:16px;display:flex;gap:4px}
.social span{width:32px;height:32px;border-radius:50%;display:block}
.s-fb{background:var(--fb)}.s-gp{background:var(--gp)}.s-tw{background:var(--tw)}.s-rss{background:var(--rss)}

.main-nav{right:20px;top:66px;display:flex;gap:20px;font-size:12px;font-weight:600;color:var(--red)}

.ribbon{position:absolute;left:145px;top:118px;width:923px;height:46px;background:var(--ribbon);border-top:1px solid #fff;border-bottom:2px solid var(--ribbon-edge);display:flex;align-items:center;padding-left:108px}
.ribbon-tail{position:absolute;top:131px}
.ribbon a{font-weight:300;font-size:16px;color:#3a3226;text-decoration:none;padding:0 14px;border-left:1px solid var(--ribbon-edge);line-height:46px}
.ribbon a:first-child{border-left:none}

.hero{left:17px;top:169px;width:582px;height:353px;background:var(--frame);border-radius:8px;padding:8px}
.hero-photo{position:relative;width:100%;height:100%;background:var(--photo)}
.hero-caption{position:absolute;left:0;right:0;bottom:0;height:40px;background:rgba(255,255,255,.55);text-align:right;padding-right:8px;font-size:17px;line-height:40px;letter-spacing:.5px;color:var(--maroon)}

.intro{left:25px;top:533px;width:570px}
.intro h1{font-weight:400;font-size:17px;color:var(--maroon);letter-spacing:.3px;margin-bottom:2px}
.intro p{font-size:11.4px;line-height:13px;color:var(--muted);margin-bottom:7px}
.intro .more{text-align:right;font-size:11.5px;color:var(--ink);font-weight:600;padding-right:8px}

.lead-panel{left:608px;top:169px;width:268px;height:498px;background:var(--frame);border-radius:8px;padding:9px}
.lead-card{background:#fff;height:100%;border:1px solid #e0d6c0;border-radius:3px;font-family:Roboto,sans-serif}
.lead-head{background:linear-gradient(#9e1a0f,#6d0d06);height:50px;color:#fff;font-weight:700;font-size:13px;text-align:center;line-height:17px;padding-top:9px}
.lead-head em{color:#f6c85a}
.lead-body{padding:11px 9px}
.lead-body p{font-size:11.3px;line-height:17px;color:#555}
.field{display:block;width:100%;height:29px;border:1px solid #c9c9c9;border-radius:3px;margin-top:4px;font-size:11.5px;color:#999;padding:6px 7px}
.field:first-of-type{margin-top:12px}
.note{margin-top:6px}
.help{display:inline-block;width:11px;height:11px;border-radius:50%;background:#2b9bc4;color:#fff;font-size:9px;line-height:11px;text-align:center;font-weight:700}
.area{height:89px;margin-top:2px!important}
.check{display:flex;align-items:center;gap:5px;font-size:11.5px;color:#555;line-height:16px}
.check i{width:11px;height:11px;border:1px solid #999;display:block}
.send{margin-left:auto;display:block;width:53px;height:25px;background:#3e3b3a;color:#fff;border-radius:3px;font-weight:700;font-size:13px;text-align:center;line-height:25px;margin-top:6px}

.section-title{font-weight:400;font-size:17px;color:var(--maroon);letter-spacing:.6px}
.listing{width:186px;height:124px;background:var(--frame);border-radius:8px;padding:7px}
.listing .photo{width:100%;height:100%;background:var(--photo-alt)}
.listing-feat{width:268px}
.place{font-size:13px;color:#2a2a2a;text-align:center;letter-spacing:.3px}
.price{font-size:30px;color:var(--red);text-align:center;letter-spacing:.5px}

.footer{left:0;bottom:0;width:892px;height:40px;background:var(--footer);color:#fff;font-size:10px;font-weight:700;text-align:center;line-height:40px}
</style>
</head>
<body>
<div class="top-band"></div>

<svg class="ribbon-tail" style="left:114px" width="32" height="48" viewBox="0 0 32 48"><polygon points="0,6 32,0 32,48 0,48 14,26" fill="#e7dcbc"/></svg>
<svg class="ribbon-tail" style="left:1068px" width="32" height="48" viewBox="0 0 32 48"><polygon points="32,6 0,0 0,48 32,48 18,26" fill="#e7dcbc"/></svg>

<div class="page">
  <div class="abs brand"><span class="brand-mark"></span><span class="brand-name">Darvy</span></div>

  <div class="abs social" aria-label="Social links">
    <span class="s-fb"></span><span class="s-gp"></span><span class="s-tw"></span><span class="s-rss"></span>
  </div>

  <nav class="abs main-nav">
    <span>Home</span><span>Auctions</span><span>Appraisals</span><span>Real Estate</span><span>FAQ’s</span><span>About Us</span><span>Contact Us</span>
  </nav>

  <div class="abs hero">
    <div class="hero-photo" role="img" aria-label="Photo of a villa with a pool and lounge chairs">
      <div class="hero-caption">Real Estate Homes for Sale in Pennsylvania</div>
    </div>
  </div>

  <section class="abs intro">
    <h1>Welcome to Real Estate Services</h1>
    <p>Lorem ipsum dolor sit amet, consectetuer adipiscing elit, sed diam nonummy nibh euismod tincidunt ut laoreet dolore magna aliquam erat volutpat. Ut wisi enim ad minim veniam, quis nostrud exerci tation ullamcorper suscipit lobortis nisl ut aliquip ex ea commodo consequat.</p>
    <p>Lorem ipsum dolor sit amet, consectetuer adipiscing elit, sed diam nonummy nibh euismod tincidunt ut laoreet dolore magna aliquam erat volutpat. Ut wisi enim ad minim veniam, quis nostrud exerci tation ullamcorper suscipit lobortis nisl ut aliquip ex ea commodo consequat.</p>
    <div class="more">Read More</div>
  </section>

  <aside class="abs lead-panel">
    <div class="lead-card">
      <div class="lead-head">FIND <em>QUALIFIED ESTATE SALE<br>COMPANIES</em> IN YOUR AREA</div>
      <div class="lead-body">
        <p>Fill out the form below and have qualified companies contact you.</p>
        <span class="field">Name</span>
        <span class="field">Zip or City &amp; State</span>
        <span class="field">Email</span>
        <span class="field">Phone</span>
        <p class="note">Size of your estate, special needs, and any additional questions. <span class="help">?</span></p>
        <span class="field area"></span>
        <p style="margin-top:12px;margin-bottom:12px">I am also interested in the following:</p>
        <div class="check"><i></i>Senior Moving Assistance</div>
        <div class="check"><i></i>Selling a Home</div>
        <span class="send">SEND</span>
      </div>
    </div>
  </aside>

  <h2 class="abs section-title" style="left:25px;top:674px">NEW LISTINGS</h2>
  <h2 class="abs section-title" style="left:616px;top:674px">FEATURED LISTING</h2>

  <div class="abs listing" style="left:17px;top:698px"><div class="photo" role="img" aria-label="Photo of a house in Harrisburg"></div></div>
  <div class="abs listing" style="left:215px;top:698px"><div class="photo" role="img" aria-label="Photo of a house in Bainbridge"></div></div>
  <div class="abs listing" style="left:413px;top:698px"><div class="photo" role="img" aria-label="Photo of a house in Elverson"></div></div>
  <div class="abs listing listing-feat" style="left:608px;top:698px"><div class="photo" role="img" aria-label="Photo of the featured family home"></div></div>

  <div class="abs place" style="left:17px;top:829px;width:186px">Harrisburg, PA</div>
  <div class="abs place" style="left:215px;top:829px;width:186px">Bainbridge, PA</div>
  <div class="abs place" style="left:413px;top:829px;width:186px">Elverson, PA</div>
  <div class="abs place" style="left:600px;top:829px;width:284px">3 Bed, 4 Bath, 4,582 Sq Ft on 2 Acres</div>

  <div class="abs price" style="left:17px;top:847px;width:186px">$209,900</div>
  <div class="abs price" style="left:215px;top:847px;width:186px">$226,900</div>
  <div class="abs price" style="left:413px;top:847px;width:186px">$389,000</div>
  <div class="abs price" style="left:608px;top:847px;width:268px">$789,000</div>

  <footer class="abs footer">© 2013 Darvy Auctioneers &amp; Appraisers.&nbsp; All rights reserved.</footer>
</div>

<nav class="ribbon">
  <a>FIND ESTATE SALES</a><a>FIND AN ESTATE SALE COMPANY</a><a>ADVERTISE AN ESTATE SALE</a>
</nav>
</body>
</html>
```